I'm looking for strong image and design for the first book in a series titled "Bernard Whitcombe On A Voyage Through Our Convictions" subtitle "Finding a Footing in Living"; although it's about beliefs, I'm not look for an ethereal feel as the first book is about how our beliefs impact our actions and expectations. I'm a published philosopher and keen on branding my name for professional purposes hence the use of my name :) The book will initially be an e-book but I will follow up with a paperback soon afterwards. My website http://bernardwhitcombe-example.com/ may provide some help on me and my projects. Thanks, Bern

Target Market(s)

Graduates and corporate folk who tend to lose their way in the systems.

Logo Text

Bernard Whitcombe on Convictions

Font styles to use
Sans Serif

Colors

Designer to choose colors to be used in the design.

Requirements
Must have
• Needless to say, but impact.
Nice to have
• Strong colours
Should not have
• Religious imagery; the book is philosophical and leans into living in this world.

```html
<!DOCTYPE html>
<html lang="en">
<head>
<meta charset="UTF-8">
<title>Bernard Whitcombe On A Voyage Through Our Convictions</title>
<link rel="stylesheet" href="https://fonts.googleapis.com/css2?family=Montserrat:wght@600;700&family=Oswald:wght@500&display=swap">
<style>
  :root {
    --purple: #a412e8;
    --violet: #4a0fc9;
    --indigo: #2a14c8;
    --blue: #1a3fd6;
    --navy: #1a158f;
    --cyan: #16e4f5;
    --white: #ffffff;
    --ink: #2b1fc2;
    --paper: #d3e6ee;
    --paper-shade: #a9c6dc;
  }
  * { margin: 0; padding: 0; box-sizing: border-box; }
  html, body { width: 800px; height: 1200px; overflow: hidden; }
  body { font-family: "Montserrat", sans-serif; }

  .cover {
    position: relative;
    width: 800px;
    height: 1200px;
    overflow: hidden;
    background:
      radial-gradient(ellipse 60% 50% at 0% 72%, rgba(10,170,230,0.95) 0%, rgba(10,170,230,0) 70%),
      radial-gradient(ellipse 60% 45% at 100% 0%, rgba(170,20,235,1) 0%, rgba(170,20,235,0) 75%),
      radial-gradient(ellipse 55% 45% at 100% 80%, rgba(26,21,143,1) 0%, rgba(26,21,143,0) 80%),
      linear-gradient(160deg, var(--violet) 0%, var(--indigo) 45%, var(--blue) 75%, #1a2fc0 100%);
  }

  .series-mark {
    position: absolute;
    top: 78px;
    left: 0;
    width: 100%;
    display: flex;
    justify-content: center;
    align-items: center;
    gap: 8px;
    font-weight: 600;
    font-size: 13px;
    letter-spacing: 1px;
    color: var(--cyan);
    text-transform: uppercase;
  }
  .series-mark .dot { width: 10px; height: 10px; border-radius: 50%; background: var(--cyan); }

  .author {
    position: absolute;
    top: 140px;
    width: 100%;
    text-align: center;
    font-weight: 600;
    color: var(--cyan);
    text-transform: uppercase;
  }
  .author .first { display: block; font-size: 90px; line-height: 96px; }
  .author .last { display: block; font-size: 76px; line-height: 92px; }

  .divider {
    position: absolute;
    top: 360px;
    left: 136px;
    width: 528px;
    display: flex;
    align-items: center;
    gap: 24px;
    color: var(--white);
    font-weight: 700;
    font-size: 24px;
  }
  .divider .rule { flex: 1; height: 3px; background: var(--white); }

  .title {
    position: absolute;
    top: 402px;
    width: 100%;
    text-align: center;
    color: var(--white);
    font-weight: 700;
    text-transform: uppercase;
  }
  .title .line-1 { display: block; font-size: 50px; line-height: 76px; }
  .title .line-2 { display: block; font-size: 54px; line-height: 76px; }

  .subtitle {
    position: absolute;
    top: 596px;
    left: 134px;
    width: 530px;
    height: 70px;
    background: linear-gradient(180deg, var(--cyan) 0%, #15c3f2 100%);
    display: flex;
    align-items: center;
    justify-content: center;
    font-family: "Oswald", sans-serif;
    font-weight: 500;
    font-size: 40px;
    color: var(--ink);
    text-transform: uppercase;
  }

  .artwork {
    position: absolute;
    left: 0;
    top: 720px;
    width: 800px;
    height: 480px;
  }
</style>
</head>
<body>
  <main class="cover">
    <div class="series-mark"><span class="dot"></span><span>Bernard Whitcombe on Convictions</span></div>

    <h1 class="author"><span class="first">Bernard</span><span class="last">Whitcombe</span></h1>

    <div class="divider"><span class="rule"></span><span>ON</span><span class="rule"></span></div>

    <h2 class="title">
      <span class="line-1">A Voyage Through</span>
      <span class="line-2">Our Convictions</span>
    </h2>

    <p class="subtitle">Finding a Footing in Living</p>

    <svg class="artwork" viewBox="0 0 800 480" role="img" aria-label="Paper butterflies cut from a pale sheet and flying up off the page">
      <defs>
        <linearGradient id="sheet-tone" x1="0" y1="0" x2="1" y2="1">
          <stop offset="0" stop-color="var(--paper)"/>
          <stop offset="1" stop-color="var(--paper-shade)"/>
        </linearGradient>
        <radialGradient id="flight-tone" cx="0.5" cy="0.5" r="0.5">
          <stop offset="0" stop-color="#cfe3ec" stop-opacity="0.55"/>
          <stop offset="1" stop-color="#cfe3ec" stop-opacity="0"/>
        </radialGradient>
      </defs>
      <ellipse cx="470" cy="140" rx="360" ry="130" fill="url(#flight-tone)"/>
      <polygon points="104,272 800,208 800,480 352,480" fill="url(#sheet-tone)"/>
    </svg>
  </main>
</body>
</html>
```